Business Card Design Project

New Business Card design for Varodine Technology Ltd using new Logo and new Tagline for staffing company.

About us from our website - www.varodine.example:

VaroDine is a leading and recognized Electronic Entertainment, Workforce Augmentation, and Project Management solutions provider with clients in Electronic Entertainment, Legal, Technology, Government and other verticals that range in size from start up organizations to Zenlar 500 companies. VaroDine is certified as an 8(a) minority and woman owned enterprise, established in 1998.

Target Market(s)

Companies in Electronic Entertainment, Legal, Government and Technology

Industry/Entity Type

Business

Requirements
Must have
• Must include in small letters the following information on back:

Established in 1998
8(a)(w)(e), Cage #7KRT9, DUNS #462137580

Front should have the following:
Derek Holloway
Vice President
5820 Birchmont Road
Fallowby, FB 482917
555-318-2746 X 100
555-902-6613 Fax
555-318-2746 Toll Free
name@varodine.example

Our Tagline: Connect • Collaborate • Achieve

```html
<!DOCTYPE html>
<html lang="en">
<head>
<meta charset="utf-8">
<title>Varodine Technology Ltd – Business Card</title>
<link href="https://fonts.googleapis.com/css2?family=Arimo:wght@400;700&display=swap" rel="stylesheet">
<style>
  :root {
    --backdrop-top: #e4e4e4;
    --backdrop-bottom: #cfcfcf;
    --card-black: #000000;
    --trim-red: #e3101b;
    --brand-blue: #1a5a9c;
    --dot-blue: #2f6fb3;
    --text-white: #ffffff;
    --text-grey: #9a9a9a;
  }
  * { box-sizing: border-box; margin: 0; padding: 0; }
  html, body {
    width: 1200px;
    height: 538px;
    overflow: hidden;
  }
  body {
    position: relative;
    background: linear-gradient(180deg, var(--backdrop-top), var(--backdrop-bottom));
    font-family: "Arimo", Arial, sans-serif;
    color: var(--text-white);
  }
  .card {
    position: absolute;
    top: 116px;
    width: 523px;
    height: 307px;
    background: var(--card-black);
    overflow: hidden;
  }
  .card--front { left: 56px; border: 2px solid var(--trim-red); }
  .card--back { left: 620px; border: 1px solid #333; }
  .card__band {
    position: absolute;
    left: 0; right: 0; bottom: 0;
    height: 16px;
    background: var(--brand-blue);
  }
  .tagline {
    position: absolute;
    left: 35px;
    top: 16px;
    font-size: 25px;
    font-weight: 700;
    letter-spacing: 0.1px;
    white-space: nowrap;
  }
  .tagline__dot {
    display: inline-block;
    width: 6px;
    height: 6px;
    margin: 0 6px;
    vertical-align: middle;
    border-radius: 50%;
    background: var(--dot-blue);
  }
  .person {
    position: absolute;
    left: 37px;
    top: 76px;
    line-height: 1.2;
  }
  .person__name { font-size: 22px; font-weight: 700; }
  .person__title, .person__company { font-size: 14.5px; }
  .person__company { margin-top: 4px; margin-left: 2px; }
  .contact {
    position: absolute;
    left: 38px;
    top: 154px;
    font-size: 14.5px;
    line-height: 17.2px;
    font-style: normal;
  }
  .brand {
    position: absolute;
    display: flex;
    align-items: center;
    gap: 8px;
    transform: translate(-50%, -50%);
    font-size: 28px;
    font-weight: 700;
    color: var(--text-white);
    white-space: nowrap;
  }
  .brand__mark {
    width: 26px;
    height: 26px;
    border-radius: 50%;
    border: 4px solid var(--brand-blue);
  }
  .card--front .brand { left: 400px; top: 153px; }
  .card--back .brand { left: 261px; top: 153px; }
  .credentials {
    position: absolute;
    left: 0; right: 0;
    top: 253px;
    text-align: center;
    font-size: 15px;
    color: var(--text-grey);
    white-space: nowrap;
  }
</style>
</head>
<body>
  <section class="card card--front" aria-label="Business card front">
    <p class="tagline">Connect<span class="tagline__dot"></span>Collaborate<span class="tagline__dot"></span>Achieve</p>
    <div class="person">
      <p class="person__name">Derek Holloway</p>
      <p class="person__title">Vice President</p>
      <p class="person__company">Varodine Technology Ltd</p>
    </div>
    <address class="contact">
      5820 Birchmont Road<br>
      Fallowby, FB 482917<br>
      555-318-2746 X 100<br>
      555-902-6613 Fax<br>
      555-318-2746 Toll Free<br>
      name@varodine.example
    </address>
    <div class="brand"><span class="brand__mark"></span>VaroDine</div>
    <div class="card__band"></div>
  </section>

  <section class="card card--back" aria-label="Business card back">
    <div class="brand"><span class="brand__mark"></span>VaroDine</div>
    <p class="credentials">Established in 1998 8(a)(w)(e), Cage #7KRT9, DUNS #462137580</p>
    <div class="card__band"></div>
  </section>
</body>
</html>
```